We need to book cover designed for publishing on Parvello.
Needs to be for a book size 6" x 9" (15.24 x 22.86 cm).
Australian Financial Planning business
Title: "Quiet Harbour: A guide to retirement planning"
Covers attached via the PDF file.

Ultimately, this cover should convey the financial planner is a steady pair of hands and is a worthy read for trusted financial advice.

The text may need to be updated after the design has been created, so flexibility to update some of the text is required.

Target Market(s)

Australian Retirees (Financial Planning Book) - will be read by individuals 50 years and older

Industry/Entity Type

Finance, Financial Planning

Colors

Designer to choose colors to be used in the design.

Requirements
Must have
• Design suitable for Parvello publishing. Needs to be for a book size 6" x 9" (15.24 x 22.86 cm). Easy to identify cover, place on the back of the cover for an image of myself and company logo.
Nice to have
• Design the book cover with similar colors used in our logo (Blue #08387B and Gold #BC9C22)

```html
<!DOCTYPE html>
<html lang="en">
<head>
<meta charset="utf-8">
<title>Quiet Harbour: A Guide to Retirement Planning</title>
<link rel="stylesheet" href="https://fonts.googleapis.com/css2?family=Bebas+Neue&display=swap">
<style>
  :root {
    --navy-top: #0b2a6a;
    --royal: #1a4fb3;
    --sky-pale: #dfe8f0;
    --cloud: #eef2f4;
    --sea: #9fb0b4;
    --sand: #d9d7d0;
    --gold-light: #fdf5a6;
    --gold-mid: #f0cf52;
    --gold-deep: #c9951a;
    --band-gold-light: #fff6a8;
    --band-gold-deep: #e2bb2e;
    --ink-blue: #1c3f96;
    --white: #ffffff;
  }
  * { margin: 0; padding: 0; box-sizing: border-box; }
  html, body { width: 798px; height: 1200px; overflow: hidden; background: #fff; }
  .cover {
    position: relative;
    width: 798px;
    height: 1200px;
    overflow: hidden;
    font-family: "Bebas Neue", "Oswald", sans-serif;
    background: linear-gradient(180deg, var(--navy-top) 0%, var(--royal) 38%, #1d55b8 55%, #2f6bc2 62%);
  }
  .beach-scene {
    position: absolute;
    left: 0; top: 650px;
    width: 798px; height: 426px;
    background: linear-gradient(180deg,
      rgba(47,107,194,0) 0%,
      #9dbbe0 10%,
      var(--sky-pale) 24%,
      var(--cloud) 55%,
      #c9d3d6 76%,
      var(--sea) 80%,
      #c4c9c6 86%,
      var(--sand) 100%);
  }
  .title-line {
    position: absolute;
    left: 0; width: 100%;
    text-align: center;
    line-height: 1;
    background: linear-gradient(180deg, var(--gold-light) 0%, var(--gold-mid) 45%, var(--gold-deep) 100%);
    -webkit-background-clip: text;
    background-clip: text;
    color: transparent;
    filter: drop-shadow(3px 4px 3px rgba(5, 20, 60, 0.55));
  }
  .title-main { font-size: 216px; }
  .title-main.first { top: 22px; }
  .title-main.second { top: 186px; font-size: 204px; }
  .subtitle-guide { top: 424px; font-size: 108px; }
  .subtitle-focus { top: 598px; font-size: 88px; letter-spacing: 1px; }
  .connector {
    position: absolute;
    top: 540px; left: 104px;
    width: 596px; height: 52px;
    display: flex; align-items: center; justify-content: space-between;
  }
  .connector .rule { width: 252px; height: 8px; background: var(--white); }
  .connector .word {
    color: var(--white);
    font-size: 62px; line-height: 1;
    padding-top: 4px;
  }
  .divider {
    position: absolute;
    left: 0; top: 1076px;
    width: 100%; height: 6px;
    background: var(--white);
  }
  .author-band {
    position: absolute;
    left: 0; top: 1082px;
    width: 100%; height: 118px;
    background: linear-gradient(180deg, var(--band-gold-light) 0%, var(--gold-mid) 55%, var(--band-gold-deep) 100%);
    display: flex; align-items: center; justify-content: center;
  }
  .author-name {
    color: var(--ink-blue);
    font-size: 84px;
    line-height: 1;
    letter-spacing: 9px;
    padding-top: 8px;
  }
</style>
</head>
<body>
  <main class="cover">
    <div class="beach-scene" role="img" aria-label="Photograph of an older couple walking barefoot together along a beach under a bright cloudy sky"></div>

    <h1>
      <span class="title-line title-main first">QUIET</span>
      <span class="title-line title-main second">HARBOUR:</span>
    </h1>
    <p class="title-line subtitle-guide">A GUIDE</p>
    <div class="connector">
      <span class="rule"></span>
      <span class="word">TO</span>
      <span class="rule"></span>
    </div>
    <p class="title-line subtitle-focus">RETIREMENT PLANNING</p>

    <div class="divider"></div>
    <div class="author-band">
      <p class="author-name">CORIN ALDOUS</p>
    </div>
  </main>
</body>
</html>
```